Saffron Lantern Court Business Card

I am looking for a business card desgined for my restaurant. It is an Indian restaurant, we are looking for something thats modern, yet traditional with the indian culture, we are looking for colors that match our logo. The logo is a design of the building with the name of the restaurant. for more information on the restaurant go to www.saffronlanterncourt.example

Industry/Entity Type

Indian Restaurant

Contact Information for Business Card

we are looking for somthing thats modern, yet traditional with the indian culture, we are looking for colors that match our logo. The logo is a design of the building with the name of the restaurant. for more information on the restaurant go to www.saffronlanterncourt.example

Requirements
Must have
• The logo that is attached,
• Name: Harvinder Oberoi,
• address of the restaurant: 7328 West Larkspur Rd, Phoenix, Arizona, 85213
• Phone: (602) 555-0147
• Fax: (602) 555-0193
• Restaurant Catering Banquet
• Website: www.SaffronLanternCourt.example
Nice to have
• wanted to get something that goes with the theme of the restaurant, which is traditional but also keep a very professional and modern touch

```html
<!DOCTYPE html>
<html lang="en">
<head>
<meta charset="utf-8">
<title>Saffron Lantern Court Business Card</title>
<link href="https://fonts.googleapis.com/css2?family=Lato:wght@400;700&display=swap" rel="stylesheet">
<style>
  :root {
    --stage: #d9d9d7;
    --card-light: #ffffff;
    --card-dark: #262626;
    --brand-red: #b1232c;
    --brand-orange: #e8621d;
    --ink: #555555;
    --pattern-light: #f4f4f4;
    --pattern-dark: #2c2c2c;
  }
  * { box-sizing: border-box; margin: 0; padding: 0; }
  html, body {
    width: 1200px; height: 1000px; overflow: hidden;
    background: var(--stage);
    font-family: "Lato", sans-serif;
  }
  .canvas { position: relative; width: 1200px; height: 1000px; }

  .card {
    position: absolute; top: 123px; width: 430px; height: 755px; overflow: hidden;
  }
  .card--front {
    left: 155px; background: var(--card-light);
    border-radius: 52px 0 52px 0;
  }
  .card--back {
    left: 615px; background: var(--card-dark);
    border-radius: 40px 40px 0 40px;
  }
  .card__pattern { position: absolute; inset: 0; }
  .card--front .card__pattern { background: radial-gradient(circle at 60% 40%, var(--pattern-light), var(--card-light) 70%); }
  .card--back .card__pattern { background: radial-gradient(circle at 50% 50%, var(--pattern-dark), var(--card-dark) 70%); }

  .brand {
    position: absolute; left: 0; right: 0; text-align: center;
  }
  .card--front .brand { top: 205px; }
  .card--back .brand { top: 360px; }
  .brand__name {
    font-weight: 700; font-size: 46px; line-height: 60px;
    letter-spacing: 3px; text-transform: uppercase; color: var(--brand-red);
  }
  .brand__since {
    margin-top: 14px; font-weight: 700; font-size: 13px;
    letter-spacing: 3px; color: var(--brand-red);
  }

  .contact { position: absolute; left: 98px; top: 500px; color: var(--ink); }
  .contact__name { font-weight: 700; font-size: 20px; color: var(--brand-orange); line-height: 24px; }
  .contact__role { font-size: 16px; line-height: 22px; }
  .contact__address { margin-top: 13px; font-size: 16px; line-height: 24px; }
  .contact__list { list-style: none; margin-top: 12px; font-size: 16px; line-height: 24px; }
  .contact__list li { display: flex; align-items: center; gap: 8px; }
  .contact__list svg { width: 13px; height: 13px; fill: var(--brand-red); flex: none; }
</style>
</head>
<body>
<main class="canvas">
  <section class="card card--front">
    <div class="card__pattern" role="img" aria-label="Faint paisley ornament pattern across the card"></div>
    <div class="brand">
      <div class="brand__name">Saffron<br>Lantern<br>Court</div>
      <div class="brand__since">SINCE 1985</div>
    </div>
    <div class="contact">
      <div class="contact__name">Harvinder Oberoi</div>
      <div class="contact__role">Founder &amp; CEO</div>
      <div class="contact__address">7328 West Larkspur Rd,<br>Phoenix, Arizona, 85213</div>
      <ul class="contact__list">
        <li><svg viewBox="0 0 16 16" aria-hidden="true"><path d="M3 1l3 3-1.5 2a9 9 0 0 0 5.5 5.5L12 10l3 3-2 2C7 15 1 9 1 3z"/></svg>(602) 555-0147</li>
        <li><svg viewBox="0 0 16 16" aria-hidden="true"><path d="M4 1h8v4H4zM1 6h14v6h-3v3H4v-3H1zM5 10v4h6v-4z"/></svg>(602) 555-0193</li>
        <li><svg viewBox="0 0 16 16" aria-hidden="true"><path d="M8 1a7 7 0 1 0 0 14A7 7 0 0 0 8 1zm-1 2v3H4.2A5 5 0 0 1 7 3zm2 0a5 5 0 0 1 2.8 3H9zM3.1 7H7v2H3.1a5 5 0 0 1 0-2zM9 7h3.9a5 5 0 0 1 0 2H9zM4.2 10H7v3a5 5 0 0 1-2.8-3zM9 10h2.8A5 5 0 0 1 9 13z"/></svg>www.SaffronLanternCourt.example</li>
      </ul>
    </div>
  </section>

  <section class="card card--back">
    <div class="card__pattern" role="img" aria-label="Faint paisley ornament pattern across the card"></div>
    <div class="brand">
      <div class="brand__name">Saffron<br>Lantern<br>Court</div>
      <div class="brand__since">SINCE 1985</div>
    </div>
  </section>
</main>
</body>
</html>
```